Webpage

I am a professional genealogist. I need a webpage that is professional looking (using the logo I chose), I can add hyperlinks and photos to if and when I want.

```html
<!DOCTYPE html>
<html lang="en">
<head>
<meta charset="utf-8">
<title>Lineage Research Services</title>
<link rel="stylesheet" href="https://fonts.googleapis.com/css2?family=Questrial&family=Arimo:wght@400;700&family=Roboto:wght@400;700&display=swap">
<style>
:root{
  --teal:#19a9c2;
  --teal-dark:#177f92;
  --mint:#b5e0d2;
  --green:#4c9a72;
  --ink:#333333;
  --text:#4a4a4a;
  --muted:#7b7b7b;
  --panel:#f1f1f1;
  --footer:#3b3b3b;
  --footer-base:#2c2c2c;
  --footer-text:#b9b9b9;
}
*{box-sizing:border-box;margin:0;padding:0}
html,body{width:970px;height:1200px;overflow:hidden;background:#fff}
body{position:relative;font-family:"Arimo",Arial,sans-serif;color:var(--text)}
a{color:inherit;text-decoration:none}

/* header */
.site-header{position:absolute;left:0;top:0;width:970px;height:131px}
.brand{position:absolute;left:43px;top:40px;display:flex;align-items:center;gap:14px}
.brand-mark{width:60px;height:60px;border-radius:50%;background:var(--mint)}
.brand-name{font-family:"Questrial",sans-serif;font-size:19px;line-height:22px;color:#3f4a4d;width:150px}
.call{position:absolute;right:42px;top:28px;font-family:"Roboto",sans-serif;font-weight:700;font-size:17px;color:var(--green)}
.search{position:absolute;left:724px;top:55px;width:204px;height:24px;background:#ececec;display:flex;align-items:center;padding-left:9px;font-size:10px;color:#6a6a6a}
.search svg{position:absolute;right:7px;top:5px}
.main-nav{position:absolute;left:398px;top:90px;width:572px;height:36px;background:var(--teal);clip-path:polygon(36px 0,100% 0,100% 100%,0 100%)}
.main-nav ul{list-style:none;display:flex;gap:0;position:absolute;right:42px;top:9px}
.main-nav li{font-family:"Questrial",sans-serif;font-size:15.5px;color:#fff;margin-left:27px}
.rule{position:absolute;left:0;width:970px;height:4px;background:var(--mint)}

/* hero */
.hero{position:absolute;left:0;top:131px;width:970px;height:324px}
.hero-photo{position:absolute;inset:0;background:linear-gradient(90deg,#d8c9bd 0%,#e9c9b4 12%,#7bb9d3 30%,#c8a58c 40%,#a9c6dc 52%,#d9cdc1 62%,#dde6ea 78%,#cfe7ef 100%)}
.hero-copy{position:absolute;left:601px;top:98px;width:330px}
.hero-copy h1{font-family:"Roboto",sans-serif;font-weight:700;font-size:20.5px;line-height:29px;color:var(--teal-dark);letter-spacing:.2px}
.hero-copy p{margin-top:6px;font-size:13px;line-height:18.5px;color:#222}
.btn{display:inline-flex;align-items:center;gap:10px;margin-top:12px;height:28px;padding:0 7px 0 15px;border-radius:14px;background:var(--teal);color:#fff;font-family:"Questrial",sans-serif;font-size:13.5px}
.dots{position:absolute;left:465px;top:303px;display:flex;gap:5px}
.dots span{width:10px;height:10px;border-radius:50%;background:#fff}
.dots span:first-child{background:var(--teal)}

/* welcome */
.welcome{position:absolute;left:0;top:460px;width:970px;height:180px;text-align:center}
.welcome h2{margin-top:20px;font-family:"Questrial",sans-serif;font-weight:400;font-size:31px;color:var(--teal);letter-spacing:1px}
.welcome .lead{margin-top:2px;font-size:14px;color:var(--muted)}
.welcome p.body{width:890px;margin:18px auto 0;font-size:11.3px;line-height:18.4px;color:var(--text)}

/* services */
.services{position:absolute;left:0;top:640px;width:970px;height:308px;background:linear-gradient(180deg,#ececec,#f6f6f6)}
.services h2{position:absolute;left:41px;top:53px;font-family:"Questrial",sans-serif;font-weight:400;font-size:24px;color:#222}
.services p{position:absolute;left:41px;top:86px;width:512px;font-size:12.2px;line-height:18.5px;color:#3c3c3c}
.services ul{position:absolute;left:49px;top:148px;list-style:none}
.services li{position:relative;padding-left:12px;font-size:12.5px;line-height:24px;color:#222}
.services li::before{content:"";position:absolute;left:0;top:9px;width:6px;height:6px;border-radius:50%;background:var(--teal)}
.services-photo{position:absolute;left:573px;top:29px;width:355px;height:246px;border:1px solid #fff;background:linear-gradient(90deg,#dcdcdc 0%,#c9b79e 25%,#9fb0a7 50%,#d2c4b6 70%,#a5bfd9 100%)}

/* footer */
.site-footer{position:absolute;left:0;top:948px;width:970px;height:204px;background:var(--footer);color:var(--footer-text)}
.site-footer h3{font-family:"Questrial",sans-serif;font-weight:400;font-size:17px;color:var(--teal);letter-spacing:.3px}
.col-nav{position:absolute;left:41px;top:17px}
.col-nav ul{list-style:none;margin-top:6px}
.col-nav li{position:relative;padding-left:14px;font-size:12px;line-height:22.8px;color:#fff}
.col-nav li::before{content:"";position:absolute;left:1px;top:8px;width:6px;height:6px;border-radius:50%;background:var(--teal)}
.col-about{position:absolute;left:193px;top:17px;width:510px}
.portrait-frame{position:absolute;left:0;top:32px;width:75px;height:75px;background:#fff;padding:6px}
.portrait{width:100%;height:100%;background:linear-gradient(180deg,#8e8a86,#b9aea4)}
.col-about p{position:absolute;left:84px;top:30px;width:424px;font-size:11.3px;line-height:15.3px}
.col-contact{position:absolute;left:724px;top:17px;width:210px}
.social{position:absolute;right:8px;top:2px;display:flex;gap:4px}
.social span{width:18px;height:18px;border-radius:50%;background:#7a7a7a}
.col-contact h4{margin-top:7px;font-family:"Questrial",sans-serif;font-weight:400;font-size:14.5px;color:#fff;letter-spacing:.3px}
.contact-row{position:absolute;left:0;display:flex;gap:10px;font-size:11.3px;line-height:15.5px;color:#fff}
.contact-row svg{flex:none;margin-top:1px}
.contact-row.text-only{padding-left:20px}
.copyright{position:absolute;left:0;top:1152px;width:970px;height:48px;background:var(--footer-base);color:#cfcfcf;font-size:11.3px;text-align:center;line-height:48px}
</style>
</head>
<body>

<header class="site-header">
  <a class="brand" href="#">
    <span class="brand-mark"></span>
    <span class="brand-name">Lineage Research Services</span>
  </a>
  <div class="call">Call: 512-555-0148</div>
  <div class="search">Enter Your Search
    <svg width="14" height="14" viewBox="0 0 14 14"><circle cx="5.5" cy="5.5" r="4.3" fill="none" stroke="#9a9a9a" stroke-width="1.8"/><line x1="8.7" y1="8.7" x2="13" y2="13" stroke="#9a9a9a" stroke-width="2"/></svg>
  </div>
  <nav class="main-nav">
    <ul>
      <li><a href="#">Home</a></li>
      <li><a href="#">About</a></li>
      <li><a href="#">Services</a></li>
      <li><a href="#">Publications</a></li>
      <li><a href="#">Blog</a></li>
      <li><a href="#">Links</a></li>
      <li><a href="#">Contact</a></li>
    </ul>
  </nav>
</header>
<div class="rule" style="top:126px"></div>

<section class="hero">
  <div class="hero-photo" role="img" aria-label="Photo of a smiling family of four in front of a faded family tree chart"></div>
  <div class="hero-copy">
    <h1>MAECENAS ULTRICES EROS EGET JUSTO ULTRICIES</h1>
    <p>Maecenas ultrices eros eget justo ultricies in mollis augue commodo. Nullam sem tortor, volutpat non eleif-end ut, adipiscing in augue.</p>
    <a class="btn" href="#">LEARN MORE
      <svg width="18" height="18" viewBox="0 0 18 18"><circle cx="9" cy="9" r="9" fill="#fff" fill-opacity=".85"/><path d="M7.5 5.5 11 9l-3.5 3.5" fill="none" stroke="#19a9c2" stroke-width="2"/></svg>
    </a>
  </div>
  <div class="dots"><span></span><span></span><span></span></div>
</section>
<div class="rule" style="top:455px"></div>

<section class="welcome">
  <h2>WELCOME</h2>
  <div class="lead">Maecenas ultrices eros eget justo ultricies</div>
  <p class="body">Maecenas ultrices eros eget justo ultricies in mollis augue commodo. Nullam sem tortor, volutpat non eleifend ut, adipiscing in augue. Aliquam at eros magna. Etiam tempus est quis massa sagittis sit amet lobortis quam malesuada. In interdum blandit ornare. Vivamus malesuada arcu in tellus consectetur rhoncus. Lorem ipsum dolor sit amet, consect-etur adipiscing elit. Pellentesque rhoncus magna in tellus luctus gravida. Donec nisl diam, imperdiet eu pulvinar eget, faucibus eu mi. Integer velit erat, blandit a ullamcorper id, volutpat et quam. Cras ornare volutpat nibh sit amet malesuada. Proin sit amet leo orci, eu molestie risus.</p>
</section>

<section class="services">
  <h2>SERVICES</h2>
  <p>Maecenas ultrices eros eget justo ultricies in mollis augue commodo. Nullam sem tortor, volutpat non eleifend ut, adipiscing in augue. Aliquam at eros magna. Etiam tempus est quis massa sagittis sit amet lobortiseu molestie risus. Quisque in magna sem. Integer in tellus felis.</p>
  <ul>
    <li>Forensic Genealogy,</li>
    <li>Kinship Determination,</li>
    <li>Research Analysis and Consultation,</li>
    <li>Texas Researcher,</li>
    <li>Record Retrieval.</li>
  </ul>
  <div class="services-photo" role="img" aria-label="Photo of a smiling man with arms crossed in front of a blurred group of people"></div>
</section>

<footer class="site-footer">
  <div class="col-nav">
    <h3>NAVIGATION</h3>
    <ul>
      <li><a href="#">Home</a></li>
      <li><a href="#">About</a></li>
      <li><a href="#">Services</a></li>
      <li><a href="#">Publications</a></li>
      <li><a href="#">Blog</a></li>
      <li><a href="#">Links</a></li>
      <li><a href="#">Contact</a></li>
    </ul>
  </div>
  <div class="col-about">
    <h3>ABOUT US</h3>
    <div class="portrait-frame"><div class="portrait" role="img" aria-label="Portrait photo of the genealogist"></div></div>
    <p>Maecenas ultrices eros eget justo ultricies in mollis augue commodo. Nullam sem tortor, volutpat non eleifend ut, adipiscing in augue. Aliquam at eros magna. Etiam tempus est quis massa sagittis sit amet lobortiseu molestie risus. Quisque in magna sem. Integer in tellus felis. Maecenas ultrices eros eget justo ultricies in mollis augue commodo. Nullam sem tortor, volutpat non eleifend ut, adipiscing in augue. Aliquam at eros magna. Etiam tempus est quis massa sagittis sit amet lobortiseu molestie risus. Quisque in magna sem. Integer in tellus felis.</p>
  </div>
  <div class="col-contact">
    <h3>CONTACT US</h3>
    <div class="social"><span></span><span></span><span></span></div>
    <h4>LINEAGE RESEARCH SERVICES</h4>
    <div class="contact-row text-only" style="top:54px">Dana Whitfield,<br>Professional Genealogist</div>
    <div class="contact-row" style="top:90px">
      <svg width="10" height="14" viewBox="0 0 10 14"><path d="M5 0a5 5 0 0 0-5 5c0 3.5 5 9 5 9s5-5.5 5-9a5 5 0 0 0-5-5zm0 7a2 2 0 1 1 0-4 2 2 0 0 1 0 4z" fill="#19a9c2"/></svg>
      <span>PO Box 40518<br>Austin, TX 78761-0518</span>
    </div>
    <div class="contact-row" style="top:131px">
      <svg width="10" height="15" viewBox="0 0 10 15"><rect x="1" y="1" width="8" height="13" rx="1.5" fill="none" stroke="#19a9c2" stroke-width="1.8"/><circle cx="5" cy="11.3" r="1" fill="#19a9c2"/></svg>
      <span>512-555-0148</span>
    </div>
    <div class="contact-row" style="top:157px">
      <svg width="13" height="10" viewBox="0 0 13 10"><rect x="0" y="1" width="13" height="9" fill="#19a9c2"/><path d="M0 1l6.5 5L13 1" fill="none" stroke="#3b3b3b" stroke-width="1.2"/></svg>
      <span>dwhitfield@example.net</span>
    </div>
  </div>
</footer>
<div class="copyright">Copyright © 2014 Lineage Research Services. All Rights Reserved.</div>

</body>
</html>
```